Medical Company in need of Modern business card design for new Wound Care clinic.

Modern business card design for our Woundcare company. Logo and description of services can be found on our website; https://www.tovrel-woundcare.com/

```html
<!DOCTYPE html>
<html lang="en">
<head>
<meta charset="utf-8">
<title>Tovrel Woundcare – Business Card</title>
<link rel="stylesheet" href="https://fonts.googleapis.com/css2?family=Poppins:wght@400;500&family=Raleway:wght@400;500;600&display=swap">
<style>
  :root {
    --stage: #5b5b5d;
    --card-dark: #1f1f1f;
    --card-dark-edge: #2a2a2a;
    --card-light: #f7f7f7;
    --gold: #c8963a;
    --gold-deep: #b07d27;
    --ink: #151515;
    --text: #222222;
  }
  * { box-sizing: border-box; margin: 0; padding: 0; }
  html, body {
    width: 900px; height: 1200px; overflow: hidden;
    background: var(--stage);
  }
  .canvas { position: relative; width: 900px; height: 1200px; }

  .card {
    position: absolute;
    left: 134px; width: 632px; height: 364px;
  }

  /* Front */
  .card-front { top: 210px; background: var(--card-dark); overflow: hidden; }
  .front-texture {
    position: absolute; inset: 0;
    background: linear-gradient(100deg, var(--card-dark) 0%, var(--card-dark) 55%, var(--card-dark-edge) 100%);
  }
  .front-mark {
    position: absolute; left: 0; right: 0; top: 163px;
    display: flex; justify-content: center; align-items: center; gap: 18px;
  }
  .front-mark .mark-dot {
    width: 10px; height: 10px; background: var(--gold);
  }
  .front-name {
    font-family: "Poppins", sans-serif; font-weight: 400;
    font-size: 37px; letter-spacing: 8px; line-height: 1;
    color: var(--gold); white-space: nowrap;
  }

  /* Back */
  .card-back { top: 624px; background: var(--card-light); text-align: center; }
  .back-name {
    position: absolute; left: 0; right: 0; top: 112px;
    font-family: "Poppins", sans-serif; font-weight: 400;
    font-size: 29px; letter-spacing: 5.5px; line-height: 1;
    color: var(--ink); white-space: nowrap;
  }
  .address {
    position: absolute; left: 0; right: 0; top: 168px;
    font-family: "Raleway", sans-serif; font-size: 14.5px; color: var(--text);
  }
  .contacts {
    position: absolute; left: 0; right: 0; top: 201px;
    display: flex; justify-content: center; gap: 18px;
    font-family: "Raleway", sans-serif; font-size: 14.5px; color: var(--text);
  }
  .contact { display: flex; align-items: center; gap: 6px; }
  .contact svg { width: 14px; height: 14px; fill: var(--gold-deep); }
  .services-title {
    position: absolute; left: 0; right: 0; top: 242px;
    font-family: "Raleway", sans-serif; font-weight: 600;
    font-size: 16.5px; color: var(--gold);
  }
  .services {
    position: absolute; left: 0; right: 0; top: 274px;
    font-family: "Raleway", sans-serif; font-size: 14.5px; line-height: 24.5px;
    color: var(--text); list-style: none;
  }
  .services .sep { font-weight: 600; margin: 0 3px; }
</style>
</head>
<body>
<div class="canvas">

  <section class="card card-front">
    <div class="front-texture" role="img" aria-label="Black card with an embossed repeating pattern of the brand symbol"></div>
    <div class="front-mark">
      <span class="mark-dot"></span>
      <span class="front-name">TOVREL WOUNDCARE</span>
    </div>
  </section>

  <section class="card card-back">
    <h1 class="back-name">TOVREL WOUNDCARE</h1>
    <p class="address">4410 Cedar Ridge Rd. Bldg. B, suite 118</p>
    <div class="contacts">
      <span class="contact">
        <svg viewBox="0 0 24 24" aria-hidden="true"><path d="M6.6 10.8a15.1 15.1 0 0 0 6.6 6.6l2.2-2.2c.3-.3.7-.4 1-.2 1.1.4 2.3.6 3.6.6.6 0 1 .4 1 1V20c0 .6-.4 1-1 1A17 17 0 0 1 3 4c0-.6.4-1 1-1h3.5c.6 0 1 .4 1 1 0 1.3.2 2.5.6 3.6.1.3 0 .7-.2 1z"/></svg>
        972-555-0142
      </span>
      <span class="contact">
        <svg viewBox="0 0 24 24" aria-hidden="true"><path d="M3 6h4v15H3zM9 3h9l3 3v15H9zm2 2v4h8V7l-2-2zm1 7v2h2v-2zm3 0v2h2v-2zm-3 3v2h2v-2zm3 0v2h2v-2z"/></svg>
        972-555-0143
      </span>
      <span class="contact">
        <svg viewBox="0 0 24 24" aria-hidden="true"><path d="M12 2a10 10 0 1 0 0 20 10 10 0 0 0 0-20zm6.9 6h-3a15 15 0 0 0-1.3-3.9A8 8 0 0 1 18.9 8zM12 4c.8 1.2 1.5 2.5 1.9 4h-3.8c.4-1.5 1.1-2.8 1.9-4zM4.3 14a8 8 0 0 1 0-4h3.4a16 16 0 0 0 0 4zm.8 2h3a15 15 0 0 0 1.3 3.9A8 8 0 0 1 5.1 16zm3-8h-3a8 8 0 0 1 4.3-3.9C8.8 5.3 8.4 6.6 8.1 8zM12 20c-.8-1.2-1.5-2.5-1.9-4h3.8c-.4 1.5-1.1 2.8-1.9 4zm2.3-6H9.7a14 14 0 0 1 0-4h4.6a14 14 0 0 1 0 4zm.3 5.9c.6-1.2 1-2.5 1.3-3.9h3a8 8 0 0 1-4.3 3.9zm1.7-5.9a16 16 0 0 0 0-4h3.4a8 8 0 0 1 0 4z"/></svg>
        www.tovrel-woundcare.com
      </span>
    </div>
    <h2 class="services-title">Our Services</h2>
    <ul class="services">
      <li>Hyperbaric Oxygen Therapy (HBO): A Cornerstone of Advanced Wound Care</li>
      <li>Debridement<span class="sep">|</span>Advanced Wound Dressings<span class="sep">|</span>Bio-engineered Skin Substitutes</li>
      <li>Compression Therapy and Edema Management</li>
    </ul>
  </section>

</div>
</body>
</html>
```